Ayurveda & Wellness Website Redesign.

I need my website www.palvoreta.com re-skinned. It is a wordpress site with Velo Framer.
I need a clearer funnel for new clients on the home page.
The funnel should provide questions for the potential client to answer. I can provide these, but I need a better funnel mechanism I think,
Possibly a video on the home page. Or an area of a video that I can change out.
So a better landing page is KEY!
The funnel should reroute to a video page and I should get informed when new clients enroll in the funnel.
Maybe I need a management system for this, but I need a recommendation.
Now I am using forms manager.
I need to be able to make changes using wordpress and/or Velo Framer.
The website should have a clean and spiritual feeling.
I can provide many more pictures and higher resolution.
I like the feeling of this website: http://brightfernherbals.com
Also this website: http://lotuscalmhaven.com/sessionswithkoriel/
Target Market(s)
Women ages 25-65. People interested in health, yoga, spirituality.
Industry/Entity Type
Health And Wellness
Coding
Coded - Design and coding required
Requirements
Must have
- A clear sales funnel/enrollment mechanism on the home page. Could have a ebook download (I will provide) when they enroll.
Nice to have
- Currently using Slotra for clients to enroll in appointments. I would like to keep this.

```html
<!DOCTYPE html>
<html lang="en">
<head>
<meta charset="utf-8">
<title>Palvoreta – Ayurveda & Wellness</title>
<link href="https://fonts.googleapis.com/css2?family=Playball&family=PT+Serif:ital,wght@0,400;0,700;1,400&display=swap" rel="stylesheet">
<style>
:root{
  --purple:#93268b;
  --purple-dark:#8a2283;
  --purple-band:#a3479c;
  --purple-bar:#9c3c96;
  --purple-soft:#b861b1;
  --pink-soft:#d9a6d4;
  --panel:#f3f3f3;
  --text:#8c8c8c;
  --white:#ffffff;
}
*{box-sizing:border-box;margin:0;padding:0}
html,body{width:1098px;height:1200px;overflow:hidden;background:var(--white)}
body{position:relative;font-family:"PT Serif",Georgia,serif;color:var(--text)}
.script{font-family:"Playball",cursive;font-weight:400}

.page-header{position:absolute;left:0;top:0;width:1098px;height:89px;background:var(--purple)}
.page-header__band{position:absolute;left:202px;width:694px;height:89px;background:var(--purple-band);display:flex;align-items:center;justify-content:center}
.page-header__title{color:var(--white);font-size:26px}

.testimonials{position:absolute;top:89px;left:0;width:1098px;height:302px}
.testimonial{position:absolute;top:55px;width:300px}
.testimonial__avatar{position:absolute;left:0;top:0;width:39px;height:39px;border-radius:50%}
.testimonial__body{position:absolute;left:54px;top:-2px;width:236px;font-size:9.2px;line-height:14.9px}
.testimonial__author{text-align:right;margin-top:10px;font-size:9.2px;padding-right:2px}
.testimonial__author em{font-style:italic}

.ayurveda{position:absolute;top:391px;left:0;width:1098px;height:297px;background:var(--panel)}
.ayurveda__media{position:absolute;left:0;top:0;width:549px;height:297px;background:linear-gradient(135deg,#4c2c5a 0%,#7a5a7e 35%,#b19a86 55%,#6c4a78 80%,#3d2744 100%)}
.play{position:absolute;left:243px;top:126px;display:flex;align-items:center;gap:6px;padding:6px 12px;background:rgba(255,255,255,.9);border-radius:4px;color:var(--purple);font-size:11px;font-weight:700}
.play__dot{width:10px;height:10px;border-radius:50%;background:var(--purple)}
.ayurveda__content{position:absolute;left:579px;top:22px;width:462px}
.ayurveda__title{color:var(--purple);font-size:28px;line-height:1}
.ayurveda__text{margin-top:16px;font-size:9.2px;line-height:14.85px}
.btn-read{position:absolute;left:0;top:243px;width:80px;height:25px;border-radius:13px;background:var(--purple);color:var(--white);font-size:7.5px;font-weight:700;display:flex;align-items:center;justify-content:center}

.strip{position:absolute;top:688px;left:0;width:1098px;height:8px;display:flex}
.strip span{flex:1}

.contact-cta{position:absolute;top:696px;left:0;width:1098px;height:295px;background:radial-gradient(ellipse at 50% 50%,#4a3428 0%,#2d211c 70%,#211814 100%)}
.contact-cta__title{position:absolute;top:76px;width:100%;text-align:center;color:var(--white);font-size:25px}
.contact-cta__text{position:absolute;left:242px;top:128px;width:614px;text-align:center;color:var(--white);font-size:9.2px;line-height:14.8px}
.btn-outline{position:absolute;left:510px;top:195px;width:80px;height:23px;border:1.5px solid var(--white);border-radius:12px;color:var(--white);font-size:7.5px;font-weight:700;display:flex;align-items:center;justify-content:center}

.info{position:absolute;top:991px;left:0;width:1098px;height:176px;background:var(--purple)}
.info__item{position:absolute;top:57px}
.info__icon{position:absolute;left:0;top:0;width:55px;height:55px;border-radius:50%;background:var(--white);display:flex;align-items:center;justify-content:center}
.info__text{position:absolute;left:74px;top:-1px;width:240px;color:#f1def0;font-size:9.2px;line-height:14.8px}
.info__heading{color:var(--white);font-size:13.5px;font-weight:700;letter-spacing:.8px;margin-bottom:7px;line-height:18px}
.info__lead{font-weight:700;color:var(--white)}

.footer-bar{position:absolute;top:1167px;left:0;width:1098px;height:33px;background:var(--purple-bar);color:#f4e3f2;font-size:6.5px}
.footer-bar__copy{position:absolute;left:202px;top:12px}
.footer-bar__social{position:absolute;left:868px;top:11px;font-size:7px;font-weight:700;color:var(--white)}
.back-top{position:absolute;left:1041px;top:3px;width:29px;height:30px;background:#b064aa;display:flex;align-items:center;justify-content:center}
</style>
</head>
<body>

<header class="page-header">
  <div class="page-header__band"><h1 class="page-header__title script">Testimonials</h1></div>
</header>

<section class="testimonials">
  <article class="testimonial" style="left:57px">
    <div class="testimonial__avatar" role="img" aria-label="Portrait photo of client M.S." style="background:#6b4a3c"></div>
    <div class="testimonial__body">
      <p>After Maren Talvik’ attentive questions, feeling of my pulses, and intuitive observation, she prescribed for me a blend of herbs and suggestions for my diet that allow me to sleep through the night without my previous fire-y constitution waking me up. Her blend of humor, humility and inquiry are a powerful combination – her very manner is one that promotes healthfulness. I have had private consultations with Maren, and have attended workshops on Ayurveda; I always learn things that are useful and applicable to my daily life, and am continually disarmed by her warmth and kindness</p>
      <p class="testimonial__author">-M.S. <em>Lorem Ipsum Dolor</em></p>
    </div>
  </article>
  <article class="testimonial" style="left:403px">
    <div class="testimonial__avatar" role="img" aria-label="Portrait photo of client D.D." style="background:#8a5a48"></div>
    <div class="testimonial__body">
      <p>My experience with Maren as my Ayurvedic practitioner far exceeded any expectation I may have had. She is exceptionally knowledgeable, and has a natural gift of sharing information in a way that is easy to understand &amp; simple to apply. Within a week of my thorough consultation with Maren I was experiencing marked &amp; measurable improvements with the issues I was struggling with. I applied her suggestions as well as other lifestyle changes. My life will never be the same &amp; that is for the better! Thanks Maren.</p>
      <p class="testimonial__author">-D.D. <em>Lorem Ipsum Dolor</em></p>
    </div>
  </article>
  <article class="testimonial" style="left:748px">
    <div class="testimonial__avatar" role="img" aria-label="Portrait photo of client J.S." style="background:#a77a62"></div>
    <div class="testimonial__body">
      <p>Maren is an attentive and insightful practitioner. The depth and breadth of her studies of Indian culture- yoga asana, health, esoteric, and practical sources all inform her practice. She has a compassionate manner, and is generous with her time and knowledge. All of these things combine to make Maren an extraordinary resource. I am exceedingly grateful for her help. .</p>
      <p class="testimonial__author">-J.S. <em>Lorem Ipsum Dolor</em></p>
    </div>
  </article>
</section>

<section class="ayurveda">
  <div class="ayurveda__media" role="img" aria-label="Video still: lavender sprigs and a kraft paper tag with the word Ayurveda">
    <div class="play"><span class="play__dot"></span>Play video</div>
  </div>
  <div class="ayurveda__content">
    <h2 class="ayurveda__title script">Ayurveda</h2>
    <p class="ayurveda__text">Ayurveda is a the “science of life.” It is a system of wellness that works with nature to correct imbalances and to maintain balance in the body,mind and spirit. Using the tools of Ayurvedic assessment (including tongue and pulse assessment) we can detect imbalances before they manifest into symptoms. Ayurveda organizes reality into three major categories that are used to understand wellness. These are the doshas. Vata dosha, which is akin to air and ether, is responsible for Flows in the body/mind: communication, transportation and movement. Pitta dosha which is likened to Fire is responsible for the Fires in the body/mind: metabolism, digestion and transformation. Kapha dosha which is like earth and water is responsible for lubrication, strength and immunity. Ayurveda works to balance these doshas via a variety of modalities including (but not limited to): meditation, nutrition, spices, herbs, herbalized oils, lifestyle recommendations, and aromatherapy. Ayurveda is a powerful system of health and well-being one that allows us to come into resonance with our own true nature.</p>
    <a class="btn-read">Read More</a>
  </div>
</section>

<div class="strip">
  <span style="background:var(--purple-dark)"></span>
  <span style="background:var(--purple-band)"></span>
  <span style="background:var(--purple-soft)"></span>
  <span style="background:var(--pink-soft)"></span>
</div>

<section class="contact-cta" role="img" aria-label="Background photo of wooden spoons filled with colourful spices on dark wood">
  <h2 class="contact-cta__title script">Get in touch now</h2>
  <p class="contact-cta__text">Lorem Ipsum is simply dummy text of the printing and typesetting industry. Lorem Ipsum has been the industry's standard dummy text ever since the 1500s, when an unknown printer took a galley of type and scrambled it to make a type specimen book. Lorem Ipsum is simply dummy text of the printing and typesetting industry. Lorem Ipsum has been the industry's standard dummy text ever since the 1500s,</p>
  <a class="btn-outline">Contact us</a>
</section>

<section class="info">
  <div class="info__item" style="left:57px">
    <div class="info__icon">
      <svg width="16" height="20" viewBox="0 0 16 20"><path d="M8 0C3.6 0 0 3.4 0 7.7 0 13 8 20 8 20s8-7 8-12.3C16 3.4 12.4 0 8 0z" fill="var(--purple)"/><circle cx="8" cy="7.5" r="2.8" fill="#fff"/></svg>
    </div>
    <div class="info__text">
      <h3 class="info__heading">Our Location</h3>
      <p><span class="info__lead">There are many variations of passages of</span><br>Lorem Ipsum available, but the majority have<br>suffered alteration in some form, by injected humour</p>
    </div>
  </div>
  <div class="info__item" style="left:458px">
    <div class="info__icon">
      <svg width="20" height="20" viewBox="0 0 24 24"><path d="M6.6 10.8c1.4 2.8 3.8 5.1 6.6 6.6l2.2-2.2c.3-.3.7-.4 1-.2 1.1.4 2.3.6 3.6.6.6 0 1 .4 1 1V20c0 .6-.4 1-1 1C10.6 21 3 13.4 3 4c0-.6.4-1 1-1h3.5c.6 0 1 .4 1 1 0 1.3.2 2.5.6 3.6.1.3 0 .7-.2 1l-2.3 2.2z" fill="var(--purple)"/></svg>
    </div>
    <div class="info__text">
      <h3 class="info__heading">Ask Our Experts</h3>
      <p>707-555-0182</p>
    </div>
  </div>
  <div class="info__item" style="left:751px">
    <div class="info__icon">
      <svg width="22" height="16" viewBox="0 0 22 16"><rect x="1" y="1" width="20" height="14" fill="none" stroke="var(--purple)" stroke-width="2"/><path d="M1 1l10 8 10-8" fill="none" stroke="var(--purple)" stroke-width="2"/></svg>
    </div>
    <div class="info__text">
      <h3 class="info__heading">Subscribe for Updates</h3>
      <p>marentalvik@mailbox.com<br>maren@palvoreta.com</p>
    </div>
  </div>
</section>

<footer class="footer-bar">
  <p class="footer-bar__copy">@2016 - Still Lotus. All rights reserved</p>
  <span class="footer-bar__social">Kindlenet</span>
  <a class="back-top" aria-label="Back to top">
    <svg width="10" height="6" viewBox="0 0 10 6"><path d="M1 5l4-4 4 4" fill="none" stroke="#fff" stroke-width="1.3"/></svg>
  </a>
</footer>

</body>
</html>
```